Premium Lawn fertiliser packaging - Looking for long term designer

*Update at bottom
I need a carefully considered, bold and professional packaging design for my new premium lawn fertiliser product. This contest is for a detailed front of the stand-up pouch packaging and once I’ve chosen a winner, they’ll be asked to create the layout for the back that links to the front as well. I have a full range of additional products that will also need designs and so I'm looking for someone who can do a great job here and who we can work with long term.

The front should include our logo for Pemberly Turf Supply Direct and be titled “Bloom Vigor Max” "Professional Lawn Fertiliser". The spring fertiliser tag line is "Awaken your lawn: Lush Greening, Lasting Health".
Beneath it, it then needs to include some important usage information and the key benefits along with some suitable graphic.

Key information to include:

Apply March - June
Treats 35-50 m2
16-3-8
+2%MgO + 1% Fe + 2.9% CaO (this is the chemical makeup of the fertiliser and needs to be fairly prominent. If you look at other professional fertiliser packaging, you'll see how it needs to compare).

Key features:
Premium fertiliser, used by professionals
Advanced greening with micro-nutrient complex
Dual action Nitrogen: Instant green boost & continuous feed for 3 months
Child & pet safe

Our brand colours are purple and green. Purple = #592999, Green = 3cb64a / 81d742 / 4d9d44

I think these colours look great against a white background.

Please make sure you look at our website as well to get an idea of our brand: www.pemberlyturfsupply.co.uk

To help, I've attached images of competitors fertiliser packaging that I like the look of. I'm not looking for you to copy but just see what type of thing appeals to me, the standard I'm expecting and what I need to compete against....

In addition, I have also attached some potential images you may wish to try using in your design, although please feel free to use your own if you have something better. For the moment, the images are 'preview' images, but once I decide on a design and we agree on the correct image, I will download and send over a fully licensed version.

*** Update*** When submitting your design, can you submit it in 2 formats: The first as a fully printed custom stand-up pouch and the second as a full-size label stuck onto a standup pouch (whatever colour you think is right for your design - choose white if you are not sure). To explain, I've just discovered we won't be able to get full custom bags printed in time for the first run and so we will have to opt for the design to be printed on labels and fixed onto bags. I therefore need to choose a design that works in both formats as both a label on a standup pouch as well as a fully printed pouch. Many thanks.

Target Market(s)

Domestic home-owners

Industry/Entity Type

Lawn care. NOT AGRICULTURE OR FARMING

Font styles to use
Sans Serif

Requirements
Must have
• Presented in 2 formats - see update at bottom of description
Nice to have
• I quite like designs against a white background, although I’m open to other ideas as well.
Should not have
• Please do not include any people or faces in the design. The text should be solid in colour, so no graduated colour fill in the text or outline text. Please avoid over-busy or cluttered designs.

```html
<!DOCTYPE html>
<html lang="en">
<head>
<meta charset="utf-8">
<title>Bloom Vigor Max – Professional Lawn Fertiliser</title>
<link href="https://fonts.googleapis.com/css2?family=Oswald:wght@700&family=Montserrat:ital,wght@0,600;0,700;1,500&family=Roboto+Condensed:ital,wght@0,500;1,500&display=swap" rel="stylesheet">
<style>
  :root {
    --purple: #592999;
    --purple-soft: #7a45c0;
    --green-bright: #81d742;
    --green-mid: #3cb64a;
    --green-deep: #4d9d44;
    --white: #ffffff;
    --backdrop: #e6e7e9;
  }
  * { margin: 0; padding: 0; box-sizing: border-box; }
  html, body {
    width: 1200px; height: 1200px; overflow: hidden;
    background: var(--backdrop);
  }
  .pouch-front {
    position: absolute; left: 300px; top: 20px;
    width: 600px; height: 1160px;
    background: var(--white);
    overflow: hidden;
    font-family: 'Montserrat', sans-serif;
  }
  .header-bands { position: absolute; inset: 0 0 auto 0; width: 600px; height: 520px; }
  .brand-name {
    position: absolute; left: 150px; top: 345px; width: 300px;
    text-align: center; color: var(--purple);
    font-family: 'Montserrat', sans-serif; font-weight: 700;
    font-size: 27px; line-height: 1.15;
  }
  .product-title {
    position: absolute; top: 530px; left: 0; width: 600px;
    text-align: center; color: var(--purple);
    font-family: 'Oswald', sans-serif; font-weight: 700;
    font-size: 64px; line-height: 1; letter-spacing: 0.5px;
    white-space: nowrap;
  }
  .product-subtitle {
    position: absolute; top: 612px; left: 0; width: 600px;
    text-align: center; color: var(--green-deep);
    font-weight: 700; font-size: 31px; white-space: nowrap;
  }
  .tagline {
    position: absolute; top: 660px; left: 70px; width: 460px; height: 30px;
    background: var(--purple); border-radius: 4px;
    color: var(--white); text-align: center; white-space: nowrap;
    font-style: italic; font-weight: 500; font-size: 16px; line-height: 30px;
  }
  .key-features {
    position: absolute; top: 702px; left: 118px; list-style: none;
    font-family: 'Roboto Condensed', sans-serif; font-style: italic; font-weight: 500;
    color: var(--green-mid); font-size: 13.5px; line-height: 19px;
  }
  .key-features li::before { content: "\2713"; margin-right: 6px; font-style: normal; }
  .scene-photo {
    position: absolute; left: 0; top: 810px; width: 600px; height: 350px;
    background:
      linear-gradient(180deg, rgba(255,255,255,0) 0%, #4f6f3a 14%, #3d5a2e 38%, #8a8f5a 52%, #9fd94a 62%, #8fd13c 100%);
  }
  .usage-info {
    position: absolute; left: 0; top: 1020px; width: 600px; text-align: center;
    font-family: 'Roboto Condensed', sans-serif; font-weight: 500; color: var(--purple);
  }
  .apply-window { font-size: 19px; }
  .coverage { margin-top: 6px; font-size: 19px; display: flex; justify-content: center; align-items: center; gap: 8px; }
  .coverage-value {
    background: var(--purple); color: var(--white);
    font-family: 'Montserrat', sans-serif; font-weight: 700;
    font-size: 26px; padding: 0 8px; line-height: 36px;
  }
  .analysis { margin-top: 6px; font-size: 19px; }
  .net-weight {
    position: absolute; right: 28px; top: 1060px;
    color: var(--white); font-family: 'Montserrat', sans-serif; font-weight: 700; font-size: 21px;
  }
</style>
</head>
<body>
  <main class="pouch-front">
    <svg class="header-bands" viewBox="0 0 600 520" aria-hidden="true">
      <path d="M0 0 H600 V380 C470 370 330 300 0 300 Z" fill="var(--green-bright)"/>
      <path d="M0 308 C200 300 380 320 600 372 V388 C380 340 200 318 0 318 Z" fill="var(--green-deep)"/>
      <path d="M0 326 C200 318 390 340 600 395 V438 C390 380 200 352 0 362 Z" fill="var(--purple-soft)"/>
      <path d="M260 440 C380 440 500 446 600 452 V500 C480 490 360 480 260 470 Z" fill="var(--green-deep)" opacity="0.85"/>
      <path d="M260 430 C380 432 500 436 600 440 V448 C500 444 380 440 260 438 Z" fill="var(--green-mid)"/>
      <ellipse cx="300" cy="385" rx="158" ry="98" fill="var(--white)" stroke="var(--purple)" stroke-width="9"/>
    </svg>
    <div class="brand-name">Pemberly Turf<br>Supply Direct</div>

    <h1 class="product-title">BLOOM VIGOR MAX</h1>
    <h2 class="product-subtitle">Professional Lawn Fertiliser</h2>
    <p class="tagline">Awaken your Lawn: Lush Greening, Lasting Health</p>

    <ul class="key-features">
      <li>Premium fertiliser, used by professionals</li>
      <li>Advanced greening with micro-nutrient complex</li>
      <li>Dual action Nitrogen: Instant green boost &amp; continuous feed for 3 months</li>
      <li>Child &amp; pet safe</li>
    </ul>

    <div class="scene-photo" role="img" aria-label="Photograph of a landscaped park with tall trees, flowering shrubs and a bright green lawn"></div>

    <section class="usage-info">
      <p class="apply-window">APPLY MARCH - JUNE</p>
      <p class="coverage">TREATS <span class="coverage-value">35-50 M2</span></p>
      <p class="analysis">16 - 3 - 8 + 2% MgO + 1% Fe + 2.9% CaO</p>
    </section>
    <p class="net-weight">10KG</p>
  </main>
</body>
</html>
```